Luxury Brand Real Estate For Sale sign

**Update** I've added some examples from the internet of other signs that have a look similar to what I would like to see. I do not want my personal name in the sign. And the word FOR SALE Does not need to be so large - it can be more subtle.
I want to create a Real Estate for sale sign for my company that will be used for luxury/higher end real estate listings. I’m sharing my business card as well as a logo with new teal color to show what we're moving towards: we’re using Teal, white, black and gold.
Hoping the sign is simple, sophisticated and eye catching.
The sign should be 24" wide by 30" tall including the company name: Harbor Crest Realty Group and our logo, office phone number 727-555-0148 and website www.hcrgexample.com the words "For Sale"
Optional to add this e-mail address info@hcrgexample.com to the sign
Target Market(s)
Luxury home buyers
Industry/Entity Type
Real Estate
Look and feel

```html
<!DOCTYPE html>
<html lang="en">
<head>
<meta charset="utf-8">
<title>Harbor Crest Realty Group — For Sale Sign</title>
<link href="https://fonts.googleapis.com/css2?family=Montserrat:wght@500;600;700;800&display=swap" rel="stylesheet">
<style>
  :root {
    --teal: #148784;
    --ink: #1b1b1b;
    --grey: #4a4a4a;
    --white: #ffffff;
    --backdrop: #eceeed;
  }
  * { margin: 0; padding: 0; box-sizing: border-box; }
  html, body {
    width: 1200px;
    height: 1200px;
    overflow: hidden;
    background: var(--backdrop);
    font-family: "Montserrat", Arial, sans-serif;
  }
  .sign {
    position: absolute;
    left: 180px;
    top: 50px;
    width: 840px;
    height: 1100px;
    background: var(--teal);
    padding: 10px 10px 0 10px;
    display: flex;
    flex-direction: column;
  }
  .sign-body {
    background: var(--white);
    height: 840px;
    display: flex;
    flex-direction: column;
    align-items: center;
  }
  .brand {
    margin-top: 108px;
    display: flex;
    align-items: center;
    gap: 26px;
  }
  .brand-square {
    width: 62px;
    height: 62px;
    background: var(--teal);
  }
  .brand-divider {
    width: 1px;
    height: 128px;
    background: var(--grey);
  }
  .brand-name {
    color: var(--teal);
    font-weight: 600;
    font-size: 44px;
    line-height: 1.12;
    letter-spacing: 0.02em;
    text-transform: uppercase;
  }
  .headline-for {
    margin-top: 112px;
    display: flex;
    align-items: center;
    gap: 18px;
  }
  .rule {
    width: 152px;
    height: 8px;
    background: var(--ink);
  }
  .for-word {
    color: var(--ink);
    font-weight: 800;
    font-size: 158px;
    line-height: 1;
    letter-spacing: 0.08em;
    margin-right: -0.08em;
  }
  .sale-word {
    margin-top: 2px;
    color: var(--teal);
    font-weight: 800;
    font-size: 280px;
    line-height: 1;
    letter-spacing: 0.01em;
  }
  .contact-band {
    flex: 1;
    display: flex;
    flex-direction: column;
    align-items: center;
    justify-content: center;
    color: var(--white);
    padding-bottom: 10px;
  }
  .phone {
    font-weight: 800;
    font-size: 98px;
    line-height: 1.05;
  }
  .website {
    margin-top: 10px;
    font-weight: 500;
    font-size: 46px;
    letter-spacing: 0.14em;
    text-transform: uppercase;
  }
</style>
</head>
<body>
  <main class="sign">
    <section class="sign-body">
      <div class="brand">
        <div class="brand-square"></div>
        <div class="brand-divider"></div>
        <div class="brand-name">Harbor Crest<br>Realty Group</div>
      </div>
      <div class="headline-for">
        <span class="rule"></span>
        <span class="for-word">FOR</span>
        <span class="rule"></span>
      </div>
      <div class="sale-word">SALE</div>
    </section>
    <section class="contact-band">
      <div class="phone">727-555-0148</div>
      <div class="website">www.hcrgexample.com</div>
    </section>
  </main>
</body>
</html>
```